Hensby Estates Website and Logo Design

We need a new logo and website designed for 'Hensby Estates Ltd', which is a well established Guernsey property holding company founded in 1934.

The company does not currently have a website. The new website should be similar in style and layout to https://www.corvanhale.org/.

Target Market(s)

Industry, Media, Tenants

Industry/Entity Type

Property Management

Logo Text

HEL OR Hensby Estates Ltd OR HE

Coding

Coded - Design and coding required

Number of Pages Required

4 page

Font styles to use
Other font styles liked:
• Helvetica

Requirements
Must have
• The logo laying over the picture (like https://www.corvanhale.org/).
• Big pictures on homepage (like https://www.corvanhale.org/)

```html
<!DOCTYPE html>
<html lang="en">
<head>
<meta charset="utf-8">
<title>Hensby Estates Ltd</title>
<link rel="stylesheet" href="https://fonts.googleapis.com/css2?family=Open+Sans:wght@400;600;700&family=Roboto+Slab:wght@400;700&family=Rokkitt:wght@400;500&display=swap">
<style>
:root{
  --teal:#1fbfb3;
  --teal-dark:#17a99e;
  --grey-bg:#efefef;
  --text:#555;
  --heading:#222;
  --footer:#222222;
  --white:#fff;
}
*{margin:0;padding:0;box-sizing:border-box}
html,body{width:1200px;height:2647px;overflow:hidden}
body{position:relative;font-family:"Open Sans",Arial,sans-serif;color:var(--text);background:var(--white)}
.abs{position:absolute}
.photo{display:block}

/* hero */
.hero{left:0;top:0;width:1200px;height:646px;background:linear-gradient(180deg,#3aa9a8 0%,#6d8f95 30%,#4c6a7a 55%,#2f5366 80%,#3d6776 100%)}
.logo{left:78px;top:20px;display:flex;align-items:center;gap:14px;color:var(--white)}
.logo-mark{width:84px;height:84px;border:3px solid var(--white);border-radius:50%}
.logo-name{font-family:"Roboto Slab",Georgia,serif;font-weight:400;font-size:34px;line-height:1.05;font-variant:small-caps}
.nav{right:78px;top:50px;display:flex;gap:52px}
.nav a{font-family:"Roboto Slab",Georgia,serif;color:var(--white);text-decoration:none;font-size:18px;letter-spacing:.5px}
.hero-title{left:0;width:1200px;top:318px;text-align:center;color:var(--white);font-family:"Roboto Slab",Georgia,serif;font-weight:700;font-size:50px;letter-spacing:1px}
.hero-sub{left:0;width:1200px;top:385px;text-align:center;color:var(--white);font-size:22px}
.btn-light{background:var(--white);color:var(--teal);border-radius:26px;font-weight:600;text-align:center;text-decoration:none}
.hero-btn{left:498px;top:442px;width:204px;height:52px;line-height:52px;font-size:17px}

/* timeline */
.timeline{left:0;top:646px;width:1200px;height:294px;background:var(--grey-bg)}
.era{width:360px;text-align:center}
.era-photo{position:absolute;width:236px;height:236px;border-radius:50%;border:6px solid var(--teal)}
.era h3{font-family:"Roboto Slab",Georgia,serif;font-weight:400;color:var(--teal);font-size:25px}
.era p{font-size:15px;line-height:25px;margin-top:8px}

/* welcome */
.welcome{left:0;top:940px;width:1200px;height:334px;background:var(--teal);color:var(--white);text-align:center}
.welcome h2{position:absolute;left:0;width:1200px;top:42px;font-family:"Rokkitt",Georgia,serif;font-weight:400;font-size:42px;font-variant:small-caps}
.welcome p{position:absolute;left:165px;width:870px;top:106px;font-size:15px;line-height:25px}
.welcome .btn-light{position:absolute;left:514px;top:233px;width:172px;height:50px;line-height:50px;font-size:18px;font-weight:400}

/* projects */
.projects{left:0;top:1274px;width:1200px;height:500px;background:linear-gradient(180deg,#f6f7f8,#eceff1)}
.section-title{position:absolute;left:0;width:1200px;text-align:center;font-family:"Rokkitt",Georgia,serif;font-weight:400;font-size:46px;color:var(--heading);font-variant:small-caps}
.section-title span{color:var(--teal)}
.projects .intro{position:absolute;left:0;width:1200px;top:118px;text-align:center;font-size:15px;line-height:25px}
.card{width:234px}
.card .photo{width:234px;height:139px}
.card h4{font-family:"Rokkitt",Georgia,serif;font-weight:400;color:var(--teal);font-size:25px;text-align:center;margin-top:16px;font-variant:small-caps;white-space:nowrap}
.card p{font-size:15px;line-height:25px;text-align:center;margin-top:6px}
.more{color:var(--text);text-decoration:none}

/* newsletter */
.newsletter{left:0;top:1774px;width:1200px;height:125px;background:var(--teal)}
.newsletter h2{position:absolute;left:203px;top:36px;font-family:"Roboto Slab",Georgia,serif;font-weight:400;font-size:40px;color:var(--white)}
.news-input{position:absolute;left:503px;top:40px;width:353px;height:46px;border:1px solid var(--white);color:var(--white);font-size:15px;line-height:44px;padding-left:10px}
.news-btn{position:absolute;left:856px;top:40px;width:141px;height:46px;background:var(--white);color:#333;font-family:"Roboto Slab",Georgia,serif;font-size:18px;line-height:46px;text-align:center}

/* news */
.news{left:0;top:1899px;width:1200px;height:494px;background:var(--white)}
.post{width:234px}
.post .photo{width:234px;height:140px}
.post h5{font-weight:400;color:var(--teal);font-size:15px;line-height:25px;margin-top:10px}
.post .date{font-size:14px;color:#999;margin-top:2px;display:flex;align-items:center;gap:6px}
.post p{font-size:15px;line-height:25px;color:#444;margin-top:4px}

/* footer */
.footer{left:0;top:2393px;width:1200px;height:201px;background:var(--footer);color:var(--white)}
.foot-nav{position:absolute;left:78px;top:20px;display:flex;gap:34px}
.foot-nav a{color:var(--white);text-decoration:none;font-size:15px}
.social{position:absolute;right:78px;top:22px;display:flex;gap:18px}
.social span{width:18px;height:18px;border-radius:50%;background:var(--white)}
.foot-rule{position:absolute;left:78px;top:71px;width:1044px;height:1px;background:#555}
.footer h6{position:absolute;left:82px;top:88px;font-family:"Roboto Slab",Georgia,serif;font-weight:400;font-size:21px;font-variant:small-caps}
.contact{position:absolute;top:128px;display:flex;align-items:center;gap:14px;font-size:15px;line-height:24px}
.contact .ico{width:40px;height:40px;border-radius:50%;flex:none;display:flex;align-items:center;justify-content:center}
.ico.teal{background:var(--teal)}
.ico.white{background:var(--white)}
.copyright{left:0;top:2594px;width:1200px;height:53px;background:var(--teal);color:var(--white);text-align:center;line-height:53px;font-size:15px}
.copyright b{font-weight:700}
</style>
</head>
<body>

<header class="abs hero" role="img" aria-label="Harbour town waterfront with moored boats and houses on the hillside"></header>
<div class="abs logo">
  <span class="logo-mark"></span>
  <span class="logo-name">Hensby Estates<br>Ltd</span>
</div>
<nav class="abs nav">
  <a href="#">HOME</a><a href="#">ABOUT</a><a href="#">PROJECTS</a><a href="#">NEWS</a><a href="#">CONTACT</a>
</nav>
<h1 class="abs hero-title">HENSBY ESTATES LTD</h1>
<p class="abs hero-sub">Lorem Ipsum is simply dummy text of the printing and typesetting industry.</p>
<a class="abs btn-light hero-btn" href="#">CONTACT US NOW</a>

<section class="abs timeline"></section>
<div class="abs era-photo" style="left:126px;top:528px;background:linear-gradient(180deg,#9cc4e4 0%,#e9ecef 45%,#3e7fa8 100%)" role="img" aria-label="Marina with white buildings and mountains"></div>
<div class="abs era-photo" style="left:486px;top:528px;background:linear-gradient(180deg,#4c7fa6 0%,#8a9aa3 50%,#3d6f8c 100%)" role="img" aria-label="Aerial view of a harbour with high rise and boats"></div>
<div class="abs era-photo" style="left:844px;top:528px;background:linear-gradient(180deg,#c9d6df 0%,#7e8c96 55%,#4e6a78 100%)" role="img" aria-label="City skyline of modern towers"></div>
<div class="abs era" style="left:64px;top:780px">
  <h3>YESTERDAY</h3>
  <p>HEL was founded in 1934 by Arthur Hensby<br>to manage both his own extensive<br>investments and his property...</p>
</div>
<div class="abs era" style="left:424px;top:780px">
  <h3>TODAY</h3>
  <p>The Hensby family has steadily built on the<br>foundations set out by the founder and<br>each generation develops and...</p>
</div>
<div class="abs era" style="left:782px;top:780px">
  <h3>TOMORROW</h3>
  <p>In keeping with its past project<br>development philosophy, its intrinsic<br>understanding of the local property mark...</p>
</div>

<section class="abs welcome">
  <h2>Welcome To Hensby Estates Ltd</h2>
  <p>Hensby Estates Limited (HEL) is a family-owned Guernsey property holding company. It purchases properties that are considered to have potential for development either through refurbishment or by obtaining planning permission to change its classification from, for example, industrial premises to offices or retail outlets, or by the marriage value of buying an adjacent property to one already owned by HEL. HEL's reputation as a fair-minded landlord...</p>
  <a class="btn-light" href="#">READ MORE &#187;</a>
</section>

<section class="abs projects">
  <h2 class="section-title" style="top:42px">Our <span>Projects</span></h2>
  <p class="intro">Lorem Ipsum is simply dummy text of the printing and typesetting industry.<br>Lorem Ipsum has a been the industry's standard.</p>
</section>
<div class="abs card" style="left:78px;top:1488px">
  <div class="photo" style="background:linear-gradient(180deg,#5d93d3 0%,#dfe6ea 55%,#4a86a8 100%)" role="img" aria-label="Marina with white buildings"></div>
  <h4>Lorem Ipsum Simply</h4>
  <p>Lorem Ipsum is simply dummy<br>text of... <a class="more" href="#">READ MORE &#187;</a></p>
</div>
<div class="abs card" style="left:348px;top:1488px">
  <div class="photo" style="background:linear-gradient(180deg,#bccad6 0%,#6f7f8a 60%,#43606d 100%)" role="img" aria-label="City skyline of towers by the water"></div>
  <h4>Lorem Ipsum Simply</h4>
  <p>Lorem Ipsum is simply dummy<br>text of... <a class="more" href="#">READ MORE &#187;</a></p>
</div>
<div class="abs card" style="left:618px;top:1488px">
  <div class="photo" style="background:linear-gradient(180deg,#4f8bd0 0%,#e3e7ea 55%,#3c7e9f 100%)" role="img" aria-label="Harbour front with boats"></div>
  <h4>Lorem Ipsum Simply</h4>
  <p>Lorem Ipsum is simply dummy<br>text of... <a class="more" href="#">READ MORE &#187;</a></p>
</div>
<div class="abs card" style="left:888px;top:1488px">
  <div class="photo" style="background:linear-gradient(180deg,#3f77a8 0%,#8696a0 50%,#356b88 100%)" role="img" aria-label="Aerial view of a marina and tower"></div>
  <h4>Lorem Ipsum Simply</h4>
  <p>Lorem Ipsum is simply dummy<br>text of... <a class="more" href="#">READ MORE &#187;</a></p>
</div>

<section class="abs newsletter">
  <h2>NEWSLETTER</h2>
  <div class="news-input">Enter Email ID</div>
  <div class="news-btn">SUBSCRIBE</div>
</section>

<section class="abs news">
  <h2 class="section-title" style="top:44px">Latest <span>News</span></h2>
</section>
<article class="abs post" style="left:78px;top:2040px">
  <div class="photo" style="background:linear-gradient(180deg,#5a9ad8 0%,#9cc0d8 50%,#4d7a6a 100%)" role="img" aria-label="Glass office building"></div>
  <h5>Lorem Ipsum is simply dummy text of the printing.</h5>
  <div class="date"><svg width="12" height="12" viewBox="0 0 12 12"><rect x="1" y="2" width="10" height="9" fill="none" stroke="#999"/><line x1="1" y1="5" x2="11" y2="5" stroke="#999"/></svg>December 2, 2016</div>
  <p>Lorem Ipsum is simply dummy text of the printing and typesetting industry.</p>
</article>
<article class="abs post" style="left:348px;top:2040px">
  <div class="photo" style="background:linear-gradient(180deg,#8ab0d6 0%,#4d6a4a 50%,#3ea0a5 100%)" role="img" aria-label="Bay with boats and green hills"></div>
  <h5>Lorem Ipsum is simply dummy text of the printing.</h5>
  <div class="date"><svg width="12" height="12" viewBox="0 0 12 12"><rect x="1" y="2" width="10" height="9" fill="none" stroke="#999"/><line x1="1" y1="5" x2="11" y2="5" stroke="#999"/></svg>December 2, 2016</div>
  <p>Lorem Ipsum is simply dummy text of the printing and typesetting industry.</p>
</article>
<article class="abs post" style="left:618px;top:2040px">
  <div class="photo" style="background:linear-gradient(180deg,#6f8296 0%,#a7a294 55%,#6b5f4c 100%)" role="img" aria-label="Riverside city with observation wheel"></div>
  <h5>Lorem Ipsum is simply dummy text of the printing.</h5>
  <div class="date"><svg width="12" height="12" viewBox="0 0 12 12"><rect x="1" y="2" width="10" height="9" fill="none" stroke="#999"/><line x1="1" y1="5" x2="11" y2="5" stroke="#999"/></svg>December 2, 2016</div>
  <p>Lorem Ipsum is simply dummy text of the printing and typesetting industry.</p>
</article>
<article class="abs post" style="left:888px;top:2040px">
  <div class="photo" style="background:linear-gradient(180deg,#9dbcd8 0%,#5b8fa8 50%,#3a6d80 100%)" role="img" aria-label="Harbour bay with moored boats"></div>
  <h5>Lorem Ipsum is simply dummy text of the printing.</h5>
  <div class="date"><svg width="12" height="12" viewBox="0 0 12 12"><rect x="1" y="2" width="10" height="9" fill="none" stroke="#999"/><line x1="1" y1="5" x2="11" y2="5" stroke="#999"/></svg>December 2, 2016</div>
  <p>Lorem Ipsum is simply dummy text of the printing and typesetting industry.</p>
</article>

<footer class="abs footer">
  <nav class="foot-nav"><a href="#">Home</a><a href="#">About</a><a href="#">Projects</a><a href="#">News</a><a href="#">Contact</a></nav>
  <div class="social"><span></span><span></span><span></span></div>
  <div class="foot-rule"></div>
  <h6>Contact Us</h6>
  <div class="contact" style="left:80px">
    <span class="ico teal"><svg width="16" height="20" viewBox="0 0 16 20"><path d="M8 1a6 6 0 0 0-6 6c0 5 6 12 6 12s6-7 6-12a6 6 0 0 0-6-6z" fill="#fff"/><circle cx="8" cy="7" r="2.3" fill="#1fbfb3"/></svg></span>
    <span>Lorem Ipsum is simply<br>dummy text</span>
  </div>
  <div class="contact" style="left:349px">
    <span class="ico white"><svg width="20" height="20" viewBox="0 0 20 20"><path d="M5 2l3 4-2 2c1 2 3 4 5 5l2-2 4 3-2 3C9 17 3 11 2 5z" fill="#1fbfb3"/></svg></span>
    <span>123 456 7890</span>
  </div>
  <div class="contact" style="left:623px">
    <span class="ico white"><svg width="20" height="20" viewBox="0 0 20 20"><rect x="3" y="7" width="14" height="10" rx="1" fill="#1fbfb3"/><rect x="6" y="3" width="8" height="5" fill="none" stroke="#1fbfb3" stroke-width="1.6"/><rect x="6" y="10" width="8" height="2" fill="#fff"/></svg></span>
    <span>123 456 7890</span>
  </div>
  <div class="contact" style="left:890px">
    <span class="ico white"><svg width="20" height="16" viewBox="0 0 20 16"><rect x="2" y="2" width="16" height="12" rx="1" fill="none" stroke="#1fbfb3" stroke-width="1.8"/><path d="M2 3l8 6 8-6" fill="none" stroke="#1fbfb3" stroke-width="1.8"/></svg></span>
    <span>Lorem Ipsum is simply</span>
  </div>
</footer>
<div class="abs copyright">&copy; <b>HENSBY ESTATES LTD - 2016.</b> All Rights Reserved.</div>

</body>
</html>
```